Business Card design for Founder and CEO of new shoe company

I am looking for a business card design for my new shoe company called Strapwell.

I am launching the company this April. Strapwell shoes offers slip-on athletic and casual style shoes for men and women. The unique selling point of the brand is that all of our shoe exist without shoelaces. I have included a link to the website to offer additional information about the company, see product images, and gain inspiration for the design. You can use the store owner password "Strapwell" to access the website.

www.Strapwell.example

Thanks,
Dan Hollis

Target Market(s)

Active Men and Women ages 16-45

Industry/Entity Type

Business

Contact Information for Business Card

Dan Hollis
Founder and CEO
www.Strapwell.example
danhollis@Strapwell.example
888-555-0187 / 888-5STRAPW
Strapwell, LLC
2284 N Tamsin Ave
Chicago, IL 60699

Requirements
Must have
• Be able to quickly and easily tell that Strapwell is a shoe company from the business card

```html
<!DOCTYPE html>
<html lang="en">
<head>
<meta charset="utf-8">
<title>Strapwell – Business Card</title>
<link rel="stylesheet" href="https://fonts.googleapis.com/css2?family=Montserrat:wght@400;700&display=swap">
<style>
  :root {
    --ink: #1b1c20;
    --paper: #ffffff;
    --backdrop: #e4e5e7;
    --blue: #4f72c3;
    --pink: #dc5a9b;
    --teal: #52c3b3;
    --photo-light: #f1f1f3;
    --photo-mid: #c9cbd3;
    --text-on-dark: #f4f4f4;
  }
  * { box-sizing: border-box; margin: 0; padding: 0; }
  html, body {
    width: 1200px; height: 900px; overflow: hidden;
    background: var(--backdrop);
    font-family: "Montserrat", Arial, sans-serif;
  }
  .canvas {
    position: relative; width: 1200px; height: 900px;
    display: flex; justify-content: center; align-items: center; gap: 120px;
  }
  .card {
    position: relative; width: 330px; height: 580px;
    background: var(--ink); overflow: hidden;
    box-shadow: 0 14px 30px rgba(0,0,0,.18);
  }

  /* Front */
  .tile { position: absolute; display: flex; align-items: center; justify-content: center; }
  .tile--blue { background: var(--blue); }
  .tile--pink { background: var(--pink); }
  .tile--teal { background: var(--teal); }
  .tile--white { background: var(--paper); }
  .tile--photo {
    background: linear-gradient(135deg, var(--photo-light) 0%, var(--photo-mid) 55%, #a7c8d8 100%);
  }
  .tile--photo.pinkish {
    background: linear-gradient(135deg, var(--photo-light) 0%, #e7b3cc 50%, #9aa3bb 100%);
  }
  .tile svg { width: 86px; height: 86px; fill: var(--ink); }
  .grid-line { position: absolute; background: var(--ink); }

  .wordmark {
    position: absolute; left: 0; right: 0; bottom: 62px;
    display: flex; align-items: center; justify-content: center; gap: 14px;
    color: var(--text-on-dark); font-size: 42px; font-weight: 400; letter-spacing: 1px;
  }
  .wordmark__mark { width: 26px; height: 26px; border: 2px solid currentColor; }

  /* Back */
  .contact-list { position: absolute; top: 92px; left: 0; right: 0; }
  .contact-row { display: flex; align-items: flex-start; height: 46px; }
  .contact-icon {
    width: 46px; height: 46px; flex: none;
    display: flex; align-items: center; justify-content: center;
  }
  .contact-icon svg { width: 24px; height: 24px; fill: none; stroke: var(--ink); stroke-width: 1.6; }
  .contact-icon--blue svg, .contact-icon--teal svg, .contact-icon--pink svg { stroke: var(--paper); }
  .contact-icon--blue { background: var(--blue); }
  .contact-icon--white { background: var(--paper); }
  .contact-icon--teal { background: var(--teal); }
  .contact-icon--pink { background: var(--pink); }
  .contact-text {
    padding: 6px 0 0 14px; color: var(--text-on-dark);
    font-size: 12px; line-height: 1.45;
  }
  .contact-name { font-weight: 700; font-size: 15px; letter-spacing: .3px; text-transform: uppercase; }
  .contact-role { font-size: 11.5px; }

  .back-band {
    position: absolute; left: 0; right: 0; bottom: 0; height: 78px;
    background: var(--paper);
    display: flex; align-items: center; padding-left: 22px; gap: 12px;
    color: var(--ink); font-size: 30px; font-weight: 400;
  }
  .back-band .wordmark__mark { width: 22px; height: 22px; border-color: var(--ink); }
</style>
</head>
<body>
<main class="canvas">

  <!-- Front of card -->
  <section class="card card--front" aria-label="Card front">
    <div class="tile tile--blue" style="left:0;top:0;width:165px;height:130px;">
      <svg viewBox="0 0 100 100" aria-hidden="true"><path d="M8 62 C10 50 20 44 30 44 L42 44 C48 40 54 34 58 30 L70 38 C72 46 80 52 92 56 C96 58 96 66 92 68 L10 68 C8 68 7 65 8 62 Z"/><rect x="8" y="70" width="86" height="6" rx="2"/></svg>
    </div>
    <div class="tile tile--white" style="left:165px;top:0;width:165px;height:65px;"></div>
    <div class="tile tile--photo" role="img" aria-label="Photo of slip-on sneakers" style="left:0;top:130px;width:165px;height:135px;"></div>
    <div class="tile tile--photo pinkish" role="img" aria-label="Photo of pink and grey sneakers" style="left:165px;top:65px;width:165px;height:135px;"></div>
    <div class="tile tile--pink" style="left:0;top:265px;width:165px;height:135px;">
      <svg viewBox="0 0 100 100" aria-hidden="true"><path d="M18 60 C18 36 34 26 50 26 C66 26 78 38 78 58 Z"/><path d="M18 60 L78 58 C84 60 92 64 90 70 C70 72 40 70 18 64 Z"/></svg>
    </div>
    <div class="tile tile--teal" style="left:165px;top:200px;width:165px;height:135px;">
      <svg viewBox="0 0 100 100" aria-hidden="true"><path d="M28 20 H44 V58 L32 74 C28 80 18 78 16 72 C14 68 18 64 20 62 L28 52 Z"/><path d="M54 26 H70 V64 L58 80 C54 86 44 84 42 78 C40 74 44 70 46 68 L54 58 Z"/></svg>
    </div>
    <div class="tile tile--photo pinkish" role="img" aria-label="Photo of a row of sneakers" style="left:165px;top:335px;width:165px;height:120px;"></div>
    <div class="grid-line" style="left:164px;top:0;width:2px;height:455px;"></div>
    <div class="grid-line" style="left:0;top:129px;width:165px;height:2px;"></div>
    <div class="grid-line" style="left:0;top:264px;width:165px;height:2px;"></div>
    <div class="grid-line" style="left:165px;top:64px;width:165px;height:2px;"></div>
    <div class="grid-line" style="left:165px;top:199px;width:165px;height:2px;"></div>
    <div class="grid-line" style="left:165px;top:334px;width:165px;height:2px;"></div>
    <div class="wordmark" style="bottom:40px;">
      <span class="wordmark__mark" aria-hidden="true"></span>
      <span class="wordmark__name">Strapwell</span>
    </div>
  </section>

  <!-- Back of card -->
  <section class="card card--back" aria-label="Card back">
    <div class="contact-list">
      <div class="contact-row">
        <div class="contact-icon contact-icon--blue">
          <svg viewBox="0 0 24 24" aria-hidden="true"><circle cx="12" cy="8" r="4"/><path d="M4 21 C4 15 20 15 20 21"/></svg>
        </div>
        <div class="contact-text">
          <div class="contact-name">Dan Hollis</div>
          <div class="contact-role">Founder and CEO</div>
        </div>
      </div>
      <div class="contact-row">
        <div class="contact-icon contact-icon--white">
          <svg viewBox="0 0 24 24" aria-hidden="true"><rect x="3" y="4" width="18" height="12"/><path d="M9 20 H15 M12 16 V20"/></svg>
        </div>
        <div class="contact-text" style="padding-top:16px;">www.Strapwell.example</div>
      </div>
      <div class="contact-row">
        <div class="contact-icon contact-icon--teal">
          <svg viewBox="0 0 24 24" aria-hidden="true"><rect x="3" y="6" width="18" height="12"/><path d="M3 6 L12 13 L21 6"/></svg>
        </div>
        <div class="contact-text" style="padding-top:16px;">danhollis@Strapwell.example</div>
      </div>
      <div class="contact-row">
        <div class="contact-icon contact-icon--white">
          <svg viewBox="0 0 24 24" aria-hidden="true"><rect x="7" y="3" width="10" height="18" rx="1.5"/><path d="M11 18 H13"/></svg>
        </div>
        <div class="contact-text" style="padding-top:16px;">888-555-0187 / 888-5STRAPW</div>
      </div>
      <div class="contact-row">
        <div class="contact-icon contact-icon--pink">
          <svg viewBox="0 0 24 24" aria-hidden="true"><path d="M12 21 C7 15 6 12 6 9 A6 6 0 0 1 18 9 C18 12 17 15 12 21 Z"/><circle cx="12" cy="9" r="2"/></svg>
        </div>
        <div class="contact-text">
          Strapwell, LLC<br>2284 N Tamsin Ave<br>Chicago, IL 60699
        </div>
      </div>
    </div>
    <div class="back-band">
      <span class="wordmark__mark" aria-hidden="true"></span>
      <span class="wordmark__name">Strapwell</span>
    </div>
  </section>

</main>
</body>
</html>
```